Bright Harbor Real Estate Institute

This must be done in word press and I will need about 7 tabs The home page, Information page, Schedule and Cost page which will link to a Email me form, a online registration a about us and location/contact tab Each tab will then open several other pages. The home page will describe different courses that we offer since all the schools are about the same you can get a good ideal by going to qelvanto.org or pinnaclebayrealtyschool.com and looking at their site I would like mine to be similar as the courses are exactly the same but I would like the site to be more modern I also need it to be in word press so I can change it and update the dates as they change I have attached he logo below

Target Market(s)

people interested in getting into real estate and those who need continuing education

Coding

Coded - Design and coding required

Number of Pages Required

5+ page

Font styles to use
Sans Serif

Colors
3276b5

Requirements
Must have
• A page to schedule classes, a tab so the college I am partnering with can link the online courses to the back side, a page that describes the type of classes I offer

```html
<!DOCTYPE html>
<html lang="en">
<head>
<meta charset="utf-8">
<title>Bright Harbor Real Estate Institute</title>
<link href="https://fonts.googleapis.com/css2?family=Roboto:wght@400;500;700&family=Noto+Serif:wght@700&display=swap" rel="stylesheet">
<style>
:root{
  --blue:#3276b5;
  --blue-dark:#2a66a0;
  --ink:#333;
  --muted:#6b6b6b;
  --topbar:#4b4b4d;
  --footer:#1d1f24;
  --line:#d6d6d6;
  --light:#f5f5f5;
}
*{margin:0;padding:0;box-sizing:border-box}
html,body{width:1200px;height:3892px;overflow:hidden}
body{font-family:'Roboto',sans-serif;color:var(--ink);background:#fff;position:relative}
a{color:inherit;text-decoration:none}
.abs{position:absolute}
.serif{font-family:'Noto Serif',serif;font-weight:700}
.media{position:absolute}

/* top bar */
.topbar{top:0;left:0;width:1200px;height:34px;background:var(--topbar);color:#fff;font-size:13px}
.topbar .contact{left:94px;top:10px;display:flex;gap:18px;align-items:center}
.topbar .right{right:94px;top:8px;display:flex;gap:10px;align-items:center}
.topbar .dot{width:17px;height:17px;border-radius:50%;background:#fff;display:inline-block}
.topbar svg{vertical-align:-3px;margin-right:5px}

/* nav */
.nav{top:34px;left:0;width:1200px;height:73px;background:#fff}
.brand{display:flex;align-items:center;gap:8px;color:var(--blue);font-family:'Noto Serif',serif;font-weight:700}
.brand .mark{border-radius:50%;background:var(--blue);flex:none}
.nav .brand{position:absolute;left:94px;top:17px;font-size:17px;line-height:1.15;width:230px}
.nav .brand .mark{width:34px;height:34px}
.menu{position:absolute;right:94px;top:29px;display:flex;gap:28px;font-size:13.5px;color:#555}
.menu .active{color:var(--blue)}

/* hero */
.hero{top:107px;left:0;width:1200px;height:493px;background:linear-gradient(180deg,#2b3038 0%,#3b3a3c 55%,#2a2420 100%)}
.hero-title{left:0;width:1200px;top:120px;text-align:center;color:#fff;font-size:48px;line-height:1.15}
.hero-title small{display:block;font-family:'Roboto',sans-serif;font-weight:500;font-size:24px;letter-spacing:1px;margin-top:4px}
.hero-text{left:200px;width:800px;top:262px;text-align:center;color:#fff;font-size:17px;line-height:29px}
.btn{display:inline-block;background:var(--blue);color:#fff;border-radius:24px;text-align:center;font-weight:500}
.hero .btn{position:absolute;left:523px;top:339px;width:154px;height:45px;line-height:45px;font-size:17px}

/* about */
.about-photo{left:94px;top:660px;width:491px;height:333px;background:linear-gradient(135deg,#8a8e94,#d8c7b5 50%,#6e7a8a)}
.about-text{left:617px;top:680px;width:490px}
.eyebrow{font-size:23px;color:#444}
.about-text h2{color:var(--blue);font-size:34px;line-height:40px;margin:2px 0 14px}
.about-text p{font-size:13px;line-height:19.5px;color:var(--muted);margin-bottom:8px}
.btn-sm{height:26px;line-height:26px;padding:0 15px;font-size:13px;margin-top:6px}

/* features */
.feature{top:1055px;width:320px;text-align:center}
.feature .icon{width:120px;height:120px;border-radius:50%;background:#e6e6e6;margin:0 auto 14px}
.feature h3{color:var(--blue);font-size:22px;margin-bottom:8px}
.feature p{font-size:13px;line-height:19.5px;color:var(--muted);padding:0 10px}
.feature a{font-size:13px;color:var(--blue);text-decoration:underline;display:block;margin-top:2px}

/* courses */
.courses{top:1357px;left:0;width:1200px;height:585px;background:var(--blue)}
.courses h2{position:absolute;left:94px;top:62px;color:#fff;font-size:42px}
.course-main{position:absolute;left:94px;top:140px;width:510px;height:360px;background:#fff}
.course-main .photo{height:236px;background:linear-gradient(120deg,#b8c9dc,#e8e2d8 50%,#8f5a4a)}
.course-main h3{color:var(--blue);font-size:17px;margin:20px 23px 6px}
.course-main p{font-size:12.5px;line-height:19px;color:var(--muted);margin:0 26px}
.course-card{position:absolute;width:228px;height:180px;background:#fff}
.course-card .photo{height:118px;background:linear-gradient(180deg,#2a2d33,#3c3f45);color:#fff;font-size:13px;text-align:center;padding-top:48px}
.course-card .photo span{text-decoration:underline}
.course-card h4{color:var(--blue);font-size:15.5px;line-height:20px;text-align:center;padding:12px 20px 0}

/* testimonials */
.testimonials{top:1942px;left:0;width:1200px;height:386px;background:#f7f7f7}
.quote-card{position:absolute;top:62px;width:492px;height:263px;border:1px solid #ccc;background:#f7f7f7}
.quote-card .avatar{position:absolute;left:22px;top:38px;width:106px;height:103px;background:linear-gradient(180deg,#eceff2,#6f7a86)}
.quote-card .qmark{position:absolute;right:40px;top:18px;font-family:'Noto Serif',serif;font-weight:700;font-size:90px;line-height:90px;color:var(--blue)}
.quote-card .who{position:absolute;left:135px;top:106px;color:var(--blue);font-size:15px}
.quote-card .who small{display:block;color:#222;font-size:10.5px;font-style:italic;margin-left:7px}
.quote-card p{position:absolute;left:22px;top:155px;width:450px;font-size:12.5px;line-height:19.5px;color:var(--muted)}

/* cta */
.cta{top:2328px;left:0;width:1200px;height:342px;background:linear-gradient(180deg,#26272b,#3a3c42 60%,#25262a);text-align:center;color:#fff}
.cta h2{position:absolute;left:0;width:1200px;top:94px;font-size:44px}
.cta p{position:absolute;left:0;width:1200px;top:158px;font-size:18px}
.cta .btn{position:absolute;left:523px;top:200px;width:150px;height:44px;line-height:44px;font-size:17px}

/* news */
.news-title{left:94px;top:2718px;color:var(--blue);font-size:42px}
.news{position:absolute;top:2800px;width:322px}
.news .photo{height:219px;position:relative}
.news .date{position:absolute;left:21px;top:33px;width:46px;height:52px;background:var(--blue);color:#fff;text-align:center;font-size:19px;line-height:20px;padding-top:6px}
.news .date small{display:block;font-size:12px}
.news h3{color:var(--blue);font-size:18px;margin:12px 0 6px}
.news p{font-size:12.5px;line-height:17px;color:var(--muted)}
.news a{display:block;margin-top:4px;font-size:13px;color:var(--blue);font-weight:500}

/* footer */
.footer{top:3286px;left:0;width:1200px;height:606px;background:linear-gradient(180deg,#1c1e23,#262930)}
.info-panel{left:94px;top:3185px;width:1012px;height:233px;background:var(--blue);border-radius:10px}
.info-box{position:absolute;top:40px;width:258px;height:148px;border:1px solid rgba(255,255,255,.7);color:#fff;text-align:center;padding-top:24px}
.info-box h4{font-size:17px;font-weight:700;margin:6px 0 3px}
.info-box p{font-size:13px;line-height:19px}
.divider{position:absolute;top:84px;width:8px;height:90px;border-left:1px solid rgba(255,255,255,.6);border-right:1px solid rgba(255,255,255,.6)}
.foot-brand{left:94px;top:3470px;color:#fff;font-size:17px;line-height:1.15;width:240px}
.foot-brand .mark{width:32px;height:32px;background:#fff}
.foot-about{left:94px;top:3575px;width:320px;color:#ddd;font-size:12.5px;line-height:19px}
.foot-col h5{color:#fff;font-size:15px;font-weight:500;margin-bottom:18px}
.post{display:flex;align-items:center;gap:12px;color:#ddd;font-size:13px;padding-bottom:13px;margin-bottom:13px;border-bottom:1px solid #555;width:150px}
.post .d{width:36px;height:32px;background:var(--blue);color:#fff;font-size:9px;text-align:center;line-height:12px;padding-top:4px;flex:none}
.sitemap li{list-style:none;color:#ddd;font-size:13px;line-height:26px}
.newsletter p{color:#ddd;font-size:12.5px;line-height:19px;width:260px}
.subscribe{margin-top:10px;width:258px;height:36px;border-radius:18px;background:#fff;position:relative;font-size:10px;color:#888;padding:12px 0 0 15px}
.subscribe .go{position:absolute;right:5px;top:5px;width:52px;height:26px;border-radius:13px;background:var(--blue)}
.socials{left:517px;top:3751px;display:flex;gap:14px}
.socials span{width:44px;height:44px;border-radius:50%;background:#c9c9c9;display:block}
.copyright{left:0;top:3833px;width:1200px;border-top:1px solid #444;text-align:center;color:#999;font-size:13px;padding-top:20px}
.copyright b{color:#ddd;font-weight:400}
</style>
</head>
<body>

<div class="abs topbar">
  <div class="abs contact">
    <span><svg width="14" height="14" viewBox="0 0 24 24" fill="none" stroke="#fff" stroke-width="2"><path d="M5 3h4l2 5-3 2a11 11 0 0 0 6 6l2-3 5 2v4a2 2 0 0 1-2 2A17 17 0 0 1 3 5a2 2 0 0 1 2-2z"/></svg>+018 - 7260 - 31</span>
    <span><svg width="14" height="14" viewBox="0 0 24 24" fill="none" stroke="#fff" stroke-width="2"><rect x="3" y="5" width="18" height="14"/><path d="M3 6l9 7 9-7"/></svg>info@brightharbor.org</span>
  </div>
  <div class="abs right">
    <span><svg width="14" height="14" viewBox="0 0 24 24" fill="none" stroke="#fff" stroke-width="2.4"><path d="M3 12h12M11 7l5 5-5 5M15 3h6v18h-6"/></svg>Login/Register</span>
    <i class="dot"></i><i class="dot"></i><i class="dot"></i>
  </div>
</div>

<header class="abs nav">
  <a class="brand"><span class="mark"></span>Bright Harbor Real Estate Institute</a>
  <nav class="menu">
    <a class="active">Home</a><a>Information</a><a>Schedule and Cost</a><a>About us</a><a>Online Registration</a><a>Location</a><a>Contact</a>
  </nav>
</header>

<section class="abs hero" role="img" aria-label="Night city skyline with lit office towers">
  <h1 class="abs hero-title serif">BRIGHT HARBOR<small>REAL ESTATE INSTITUTE</small></h1>
  <p class="abs hero-text">It is a long established fact that a reader will be distracted by the readable content of a page when looking at its layout. The point of using Lorem Ipsum</p>
  <a class="btn">Contact Us</a>
</section>

<div class="media about-photo" role="img" aria-label="Smiling instructor holding folders in a classroom with students"></div>
<div class="abs about-text">
  <div class="eyebrow">About Us</div>
  <h2 class="serif">Bright Harbor Real Estate Institute</h2>
  <p>It is a long established fact that a reader will be distracted by the readable content of a page when looking at its layout. The point of using Lorem Ipsum is that it has a more-or-less normal distribution of letters, as opposed to using 'Content here, content here', making it look like readable English.</p>
  <p>There are many variations of passages of Lorem Ipsum available, but the majority have suffered alteration in some form....</p>
  <a class="btn btn-sm">Read More</a>
</div>

<div class="abs feature" style="left:94px">
  <div class="icon" role="img" aria-label="Illustration of a person working at a computer"></div>
  <h3 class="serif">Information</h3>
  <p>Lorem Ipsum is simply dummy text of the printing and typesetting industry. Lorem Ipsum has been the industry's standard</p>
  <a>Read More</a>
</div>
<div class="abs feature" style="left:439px">
  <div class="icon" role="img" aria-label="Illustration of a money bag and coins"></div>
  <h3 class="serif">Schedule &amp; Cost</h3>
  <p>Lorem Ipsum is simply dummy text of the printing and typesetting industry. Lorem Ipsum has been the industry's standard</p>
  <a>Read More</a>
</div>
<div class="abs feature" style="left:784px">
  <div class="icon" role="img" aria-label="Illustration of an online registration form"></div>
  <h3 class="serif">Online Registration</h3>
  <p>Lorem Ipsum is simply dummy text of the printing and typesetting industry. Lorem Ipsum has been the industry's standard</p>
  <a>Read More</a>
</div>

<section class="abs courses">
  <h2 class="serif">Online Courses</h2>
  <article class="course-main">
    <div class="photo" role="img" aria-label="Students writing at desks in a classroom"></div>
    <h3 class="serif">There are many variations</h3>
    <p>Lorem Ipsum is simply dummy text of the printing and typesetting industry. Lorem Ipsum has been the industry's standard dummy text ever since the 1500s,</p>
  </article>
  <article class="course-card" style="left:627px;top:128px"><div class="photo" role="img" aria-label="Dark classroom photo"><span>Read More</span></div><h4 class="serif">Contrary to popular belief</h4></article>
  <article class="course-card" style="left:878px;top:128px"><div class="photo" role="img" aria-label="Dark classroom photo"><span>Read More</span></div><h4 class="serif">Contrary to popular belief</h4></article>
  <article class="course-card" style="left:627px;top:326px"><div class="photo" role="img" aria-label="Dark classroom photo"><span>Read More</span></div><h4 class="serif">Contrary to popular belief</h4></article>
  <article class="course-card" style="left:878px;top:326px"><div class="photo" role="img" aria-label="Dark classroom photo"><span>Read More</span></div><h4 class="serif">Contrary to popular belief</h4></article>
</section>

<section class="abs testimonials">
  <div class="quote-card" style="left:94px">
    <div class="avatar" role="img" aria-label="Portrait of a businesswoman"></div>
    <div class="qmark">”</div>
    <div class="who">-Lorem Ipsum<small>Contrary to</small></div>
    <p>It is a long established fact that a reader will be distracted by the readable content of a page when looking at its layout. The point of using Lorem Ipsum is that it has a more-or-less normal distribution of letters, as opposed to using......</p>
  </div>
  <div class="quote-card" style="left:613px">
    <div class="avatar" role="img" aria-label="Portrait of a businessman"></div>
    <div class="qmark">”</div>
    <div class="who">-Lorem Ipsum<small>Contrary to</small></div>
    <p>It is a long established fact that a reader will be distracted by the readable content of a page when looking at its layout. The point of using Lorem Ipsum is that it has a more-or-less normal distribution of letters, as opposed to using......</p>
  </div>
</section>

<section class="abs cta" role="img" aria-label="Students in a lecture hall, darkened">
  <h2 class="serif">There are many variations of passages</h2>
  <p>Lorem Ipsum is simply dummy text of the printing and typesetting industry.</p>
  <a class="btn">Join Now</a>
</section>

<h2 class="abs news-title serif">Latest News</h2>
<article class="news" style="left:94px">
  <div class="photo" role="img" aria-label="Row of computers on a desk" style="background:linear-gradient(135deg,#9aa3ad,#e2e0dc 60%,#c89a5c)"><div class="date">31<small>July</small></div></div>
  <h3 class="serif">Contrary to popular belief</h3>
  <p>Lorem Ipsum is simply dummy text of the printing and typesetting industry. Lorem Ipsum has been the industry's...</p>
  <a>Read More »</a>
</article>
<article class="news" style="left:440px">
  <div class="photo" role="img" aria-label="Hands clapping against a dark background" style="background:linear-gradient(135deg,#2a2a2c,#8a6a55 55%,#2f2f31)"><div class="date">31<small>July</small></div></div>
  <h3 class="serif">Contrary to popular belief</h3>
  <p>Lorem Ipsum is simply dummy text of the printing and typesetting industry. Lorem Ipsum has been the industry's...</p>
  <a>Read More »</a>
</article>
<article class="news" style="left:784px">
  <div class="photo" role="img" aria-label="Books, pencils and an apple in a library" style="background:linear-gradient(135deg,#5a3f2f,#b58a5e 50%,#3e2c22)"><div class="date">31<small>July</small></div></div>
  <h3 class="serif">Contrary to popular belief</h3>
  <p>Lorem Ipsum is simply dummy text of the printing and typesetting industry. Lorem Ipsum has been the industry's...</p>
  <a>Read More »</a>
</article>

<footer class="abs footer" role="img" aria-label="Darkened photo of students studying"></footer>

<div class="abs info-panel">
  <div class="info-box" style="left:71px">
    <svg width="22" height="26" viewBox="0 0 24 28" fill="#fff"><path d="M12 0a9 9 0 0 0-9 9c0 7 9 17 9 17s9-10 9-17a9 9 0 0 0-9-9zm0 13a4 4 0 1 1 0-8 4 4 0 0 1 0 8z"/></svg>
    <h4>Address</h4><p>218 Lantern Mill Road<br>Harborview, Maine</p>
  </div>
  <div class="divider" style="left:350px"></div>
  <div class="info-box" style="left:378px">
    <svg width="26" height="26" viewBox="0 0 24 24" fill="none" stroke="#fff" stroke-width="2"><path d="M5 3h4l2 5-3 2a11 11 0 0 0 6 6l2-3 5 2v4a2 2 0 0 1-2 2A17 17 0 0 1 3 5a2 2 0 0 1 2-2z"/></svg>
    <h4>Phone Number</h4><p>+018 7260 31<br>+018 4915 62</p>
  </div>
  <div class="divider" style="left:656px"></div>
  <div class="info-box" style="left:683px">
    <svg width="28" height="22" viewBox="0 0 28 20" fill="#fff"><path d="M0 0h28v3L14 11 0 3zM0 6l14 8 14-8v14H0z"/></svg>
    <h4>Email Address</h4><p>Email:<br>info@brightharbor.org</p>
  </div>
</div>

<a class="abs brand foot-brand"><span class="mark"></span>Bright Harbor Real Estate Institute</a>
<p class="abs foot-about">Lorem Ipsum is simply dummy text of the printing and typesetting industry. Lorem Ipsum has been the industry's standard dummy text ever since the 1500s,</p>

<div class="abs foot-col" style="left:456px;top:3494px">
  <h5>Recent Posts</h5>
  <div class="post"><span class="d">14<br>2018</span>There are many</div>
  <div class="post" style="border:0"><span class="d">14<br>2018</span>There are many</div>
</div>
<div class="abs foot-col sitemap" style="left:666px;top:3494px">
  <h5 style="margin-bottom:8px">Our Sitemap</h5>
  <ul><li>» Home</li><li>» Information</li><li>» Schedule and Cost</li><li>» About us</li><li>» Online Registration</li><li>» Location</li><li>» Contact</li></ul>
</div>
<div class="abs foot-col newsletter" style="left:848px;top:3494px">
  <h5 style="margin-bottom:12px">Newsletter</h5>
  <p>It is a long established fact that a reader will be distracted</p>
  <div class="subscribe">Your email address<span class="go"><svg width="52" height="26" viewBox="0 0 52 26"><path d="M19 13l14-6-4 13-3-5z" fill="#fff"/></svg></span></div>
</div>

<div class="abs socials"><span></span><span></span><span></span></div>
<div class="abs copyright">© 2019 <b>Bright Harbor Real Estate Institute</b>. All Rights Reserved</div>

</body>
</html>
```